"Dario Quillon" Business Card

Friends

My name is "Dario Quillon" and I need your help! I need a new business card for my personal use.

As background, "Dario Quillon" is actually an alias that I use when I meet women. Please use your creative skills to create an amazing business card for me to use!

In addition to including my name and contact details (see the "Must Have" section), you may wish to add a catchphrase or a title if you think it would help me :)

For background, please see:

http://www.dailybrightwire.com/2013/07/23/morton-feld-dario-quillon_n_5129847.html

Looking forward to seeing what you can do for me.

Hugs and kisses,

Dario Quillon [courtesy of PixelHarbor]

Target Market(s)

Adult women in New York City...or anywhere really.

Industry/Entity Type

Business

Requirements
Must have
• Please include the following details:

Dario Quillon
P: +1-555-3QUILLN
E: secrets@darioquillon-mail.com
Nice to have
• You might include a catchphrase, like "Quillon is my surname But you can call me Mr Smoothstep".

Or perhaps a title, like "Dario Quillon, Head of Sexy Times".

You're creative...I will leave the details to you my friends.
Should not have
• Any references to my actual name...because then, what's the point in using an alias?

```html
<!DOCTYPE html>
<html lang="en">
<head>
<meta charset="utf-8">
<title>Dario Quillon — Business Card</title>
<link rel="stylesheet" href="https://fonts.googleapis.com/css2?family=Marcellus&family=Marcellus+SC&family=Quicksand:wght@400;500&display=swap">
<style>
  :root {
    --backdrop: #2a2a2a;
    --card-dark: #0b0b0c;
    --card-mid: #202224;
    --ink: #f2f2f2;
    --ink-soft: #d8d8d8;
    --divider-dark: rgba(0,0,0,0.75);
    --divider-light: rgba(255,255,255,0.05);
  }
  html, body {
    margin: 0;
    padding: 0;
    width: 1029px;
    height: 1200px;
    overflow: hidden;
    background: var(--backdrop);
  }
  .canvas {
    position: relative;
    width: 1029px;
    height: 1200px;
  }
  .card {
    position: absolute;
    left: 190px;
    width: 632px;
    height: 344px;
    background:
      radial-gradient(ellipse 45% 70% at 50% 45%, var(--card-mid) 0%, rgba(20,20,22,0.6) 55%, transparent 100%),
      linear-gradient(90deg, var(--card-dark) 0%, #141516 35%, #141516 65%, var(--card-dark) 100%);
    box-shadow: 0 4px 14px rgba(0,0,0,0.55);
    overflow: hidden;
  }
  .card--front { top: 53px; }
  .card--contact { top: 426px; }
  .card--title { top: 799px; }

  .divider {
    position: absolute;
    width: 2px;
    background: linear-gradient(180deg, transparent, var(--divider-dark) 30%, var(--divider-dark) 70%, transparent);
    box-shadow: 1px 0 0 var(--divider-light);
  }

  .name {
    position: absolute;
    font-family: "Marcellus", serif;
    color: var(--ink);
    white-space: nowrap;
    letter-spacing: -0.5px;
    line-height: 1;
  }
  .title {
    position: absolute;
    font-family: "Marcellus SC", serif;
    color: var(--ink-soft);
    white-space: nowrap;
    line-height: 1;
  }

  /* front */
  .card--front .name { right: 338px; top: 143px; font-size: 30px; }
  .card--front .title { right: 340px; top: 181px; font-size: 11px; letter-spacing: 1px; }
  .card--front .divider { left: 317px; top: 108px; height: 150px; }
  .wordmark {
    position: absolute;
    left: 341px;
    top: 146px;
    font-family: "Marcellus", serif;
    font-size: 30px;
    color: #c9c9c9;
    white-space: nowrap;
    line-height: 1;
  }

  /* contact */
  .card--contact .divider { left: 343px; top: 88px; height: 180px; }
  .contact-line {
    position: absolute;
    right: 304px;
    font-family: "Quicksand", sans-serif;
    font-size: 13px;
    color: var(--ink-soft);
    white-space: nowrap;
    line-height: 1;
  }
  .contact-line--phone { top: 149px; }
  .contact-line--email { top: 181px; letter-spacing: 0.5px; }
  .contact-icon { position: absolute; left: 358px; width: 20px; height: 16px; }
  .contact-icon--phone { top: 146px; }
  .contact-icon--email { top: 178px; }
  .catchphrase {
    position: absolute;
    right: 14px;
    bottom: 11px;
    font-family: "Marcellus SC", serif;
    font-size: 11px;
    color: var(--ink-soft);
    white-space: nowrap;
    letter-spacing: 0.3px;
  }

  /* title card */
  .card--title .name { left: 45px; top: 152px; font-size: 37px; }
  .card--title .divider { left: 318px; top: 95px; height: 170px; }
  .card--title .title { left: 355px; top: 161px; font-size: 17px; letter-spacing: 1.5px; color: var(--ink); }
</style>
</head>
<body>
<main class="canvas">
  <section class="card card--front">
    <div class="name">Dario Quillon</div>
    <div class="title">Head of Sexy Times</div>
    <div class="divider"></div>
    <div class="wordmark">Dario Quillon</div>
  </section>

  <section class="card card--contact">
    <div class="contact-line contact-line--phone">+1-555-3QUILLN</div>
    <div class="contact-line contact-line--email">secrets@darioquillon-mail.com</div>
    <div class="divider"></div>
    <svg class="contact-icon contact-icon--phone" viewBox="0 0 20 16" aria-label="Phone">
      <path d="M1 5 Q10 -1 19 5 L17 7 L14 6 L14 4 Q10 3 6 4 L6 6 L3 7 Z" fill="#eee"/>
      <path d="M4 8 L16 8 L18 15 L2 15 Z" fill="#eee"/>
      <circle cx="10" cy="11.5" r="2" fill="#141516"/>
    </svg>
    <svg class="contact-icon contact-icon--email" viewBox="0 0 20 16" aria-label="Email">
      <rect x="1" y="2" width="18" height="12" fill="#eee"/>
      <path d="M1 2 L10 9 L19 2" fill="none" stroke="#141516" stroke-width="1.2"/>
      <path d="M1 14 L8 7.5 M19 14 L12 7.5" stroke="#141516" stroke-width="1"/>
    </svg>
    <div class="catchphrase">Quillon is my surname But you can call me Mr Smoothstep</div>
  </section>

  <section class="card card--title">
    <div class="name">Dario Quillon</div>
    <div class="divider"></div>
    <div class="title">Head of Sexy Times</div>
  </section>
</main>
</body>
</html>
```